Design some Business Cards for Brevond Travel

Attached is the current business card. Just need a better looking card. All detail should remain the same.

GRVU logo and the address and phone details remain the same - everything else you can play around with.

Emphasis on company name please.

Thanks

```html
<!DOCTYPE html>
<html lang="en">
<head>
<meta charset="utf-8">
<title>Brevond Travel – Business Cards</title>
<link rel="stylesheet" href="https://fonts.googleapis.com/css2?family=Cinzel:wght@400;600&display=swap">
<style>
  :root {
    --sand: #dcc27e;
    --royal: #2b3f9e;
    --royal-light: #3147a8;
    --gold: #d2b26e;
    --gold-soft: #e6cf95;
    --copper: #a8623a;
    --ink: #2b3f9e;
  }
  * { margin: 0; padding: 0; box-sizing: border-box; }
  html, body { width: 1200px; height: 899px; overflow: hidden; }
  body {
    background: var(--sand);
    font-family: "Cinzel", "Times New Roman", serif;
    position: relative;
  }

  /* Front card */
  .card-front {
    position: absolute; left: 17px; top: 10px; width: 759px; height: 420px;
    background: var(--royal);
  }
  .brand-panel {
    position: absolute; left: 120px; top: 90px; width: 535px; height: 216px;
    background: var(--royal-light);
    box-shadow: 0 10px 22px rgba(10, 20, 70, .55);
    display: flex; align-items: center; justify-content: center; gap: 14px;
  }
  .brand-mark {
    width: 84px; height: 84px; border-radius: 50%;
    border: 3px solid var(--gold);
  }
  .brand-words { color: var(--gold); line-height: 1; font-weight: 400; }
  .brand-name { font-size: 48px; font-weight: 600; letter-spacing: 1px; display: block; }
  .brand-service { font-size: 28px; font-weight: 400; letter-spacing: 1px; display: block; margin-top: 4px; }

  .tagline-ribbon {
    position: absolute; height: 40px;
    background: linear-gradient(90deg, rgba(168,98,58,0) 0%, var(--copper) 18%, #c98a5c 50%, var(--copper) 82%, rgba(168,98,58,0) 100%);
    color: var(--gold-soft);
    font-size: 24px; letter-spacing: 1px;
    display: flex; align-items: center; justify-content: center;
  }
  .card-front .tagline-ribbon { left: 243px; top: 335px; width: 306px; }

  /* Back card */
  .card-back {
    position: absolute; left: 402px; top: 454px; width: 756px; height: 418px;
    background: var(--royal);
  }
  .back-panel {
    position: absolute; left: 33px; top: 25px; width: 690px; height: 364px;
    background: var(--sand);
    box-shadow: 0 6px 16px rgba(10, 20, 70, .45);
    overflow: hidden;
  }
  .name-band { position: absolute; left: 0; top: 0; width: 690px; height: 160px; }
  .badge {
    position: absolute; left: 22px; top: 20px; width: 58px; height: 58px;
    border-radius: 50%; background: var(--sand); border: 3px solid var(--gold);
  }
  .person-name {
    position: absolute; left: 100px; right: 0; top: 64px; text-align: center;
    color: var(--gold); font-size: 50px; font-weight: 400; letter-spacing: 2px; line-height: 1;
    white-space: nowrap;
  }
  .divider {
    position: absolute; left: 347px; top: 170px; width: 3px; height: 140px;
    background: var(--royal);
  }
  .contact-list { position: absolute; list-style: none; color: var(--ink); }
  .contact-list li { display: flex; align-items: center; gap: 8px; white-space: nowrap; }
  .contact-list svg { width: 20px; height: 20px; fill: var(--ink); flex: none; }
  .contacts-left { left: 86px; top: 195px; }
  .contacts-left li { font-size: 23px; height: 32px; }
  .contacts-left li.email { font-size: 15px; letter-spacing: .5px; }
  .contacts-right { left: 436px; top: 195px; }
  .contacts-right li { font-size: 23px; height: 32px; }
  .contacts-right .country { font-size: 12px; margin-right: 2px; }
  .contacts-right li.address { align-items: flex-start; font-size: 15px; line-height: 1.2; height: auto; margin-top: 2px; }
  .card-back .tagline-ribbon { left: 200px; top: 322px; width: 318px; height: 36px; font-size: 22px; }
</style>
</head>
<body>

<section class="card-front" aria-label="Card front">
  <div class="brand-panel">
    <span class="brand-mark" aria-hidden="true"></span>
    <h1 class="brand-words">
      <span class="brand-name">BREVOND</span>
      <span class="brand-service">HAJJ &amp; UMRAH</span>
    </h1>
  </div>
  <p class="tagline-ribbon">WORL WIDE TRAVEL</p>
</section>

<section class="card-back" aria-label="Card back">
  <div class="back-panel">
    <svg class="name-band" viewBox="0 0 690 160" aria-hidden="true">
      <polygon points="0,0 690,0 690,156 370,156 348,135 326,156 0,156" fill="#2b3f9e"/>
    </svg>
    <span class="badge" aria-hidden="true"></span>
    <h2 class="person-name">HAMID RASHELI</h2>

    <ul class="contact-list contacts-left">
      <li>
        <svg viewBox="0 0 24 24" aria-hidden="true"><path d="M6.6 10.8a15 15 0 0 0 6.6 6.6l2.2-2.2a1 1 0 0 1 1-.25 11.4 11.4 0 0 0 3.6.57 1 1 0 0 1 1 1V20a1 1 0 0 1-1 1A17 17 0 0 1 3 4a1 1 0 0 1 1-1h3.5a1 1 0 0 1 1 1c0 1.25.2 2.45.57 3.57a1 1 0 0 1-.25 1z"/></svg>
        0120 480 3317
      </li>
      <li>
        <svg viewBox="0 0 24 24" aria-hidden="true"><path d="M7 2h10v6H7zM4 9h16a2 2 0 0 1 2 2v7h-4v4H6v-4H2v-7a2 2 0 0 1 2-2zm4 7v4h8v-4z"/></svg>
        0120 480 3318
      </li>
      <li class="email">
        <svg viewBox="0 0 24 24" aria-hidden="true"><path d="M3 6h18v12H3zm2 2v.4l7 4.4 7-4.4V8l-7 4.4z"/></svg>
        BREVOND@MAILNET.COM
      </li>
    </ul>

    <div class="divider" aria-hidden="true"></div>

    <ul class="contact-list contacts-right">
      <li>
        <svg viewBox="0 0 24 24" aria-hidden="true"><path d="M6.6 10.8a15 15 0 0 0 6.6 6.6l2.2-2.2a1 1 0 0 1 1-.25 11.4 11.4 0 0 0 3.6.57 1 1 0 0 1 1 1V20a1 1 0 0 1-1 1A17 17 0 0 1 3 4a1 1 0 0 1 1-1h3.5a1 1 0 0 1 1 1c0 1.25.2 2.45.57 3.57a1 1 0 0 1-.25 1z"/></svg>
        0700 5180 266
      </li>
      <li><span class="country">SAUDI</span> 2500 7731 48</li>
      <li class="address">
        <svg viewBox="0 0 24 24" aria-hidden="true"><path d="M12 2a7 7 0 0 0-7 7c0 5 7 13 7 13s7-8 7-13a7 7 0 0 0-7-7zm0 9.5A2.5 2.5 0 1 1 12 6.5a2.5 2.5 0 0 1 0 5z"/></svg>
        <span>17, ASH VALE DUNMORE<br>DN4 2QA U.K</span>
      </li>
    </ul>

    <p class="tagline-ribbon">WORL WIDE TRAVEL</p>
  </div>
</section>

</body>
</html>
```